Presentation Folder Design for Photographer

Professional photographer requires a presentation folder for marketing.
I specialise in architecture, corporate & commercial photography. The folder will be used to promote my architectural photography services to real estate, accomodation & architect clients.

I'm looking for a modern clean design that complements my logo with complimentary text & colours. I want to use some images in the design, probably a mix of images not just architectural. I need a print ready design in PDF as well as a PSD file that I can possibly edit / update images later on.

The folder will be a double sided design with no need for pockets included in the design. Overall dimensions are 430mm ( folded down the centre ) x 315mm with a 5mm trim & bleed.

The layout would be as follows :

Front cover - Logo + maybe some images or some other design work.

Inside front cover - Some text about my services.

ARCHITECTURE
Commercial Residential Real Estate Drone Floorpans Accommodation

CORPORATE
Studio Headshots Environmental Portraits Staff Photography

COMMERCIAL
Product Advertising Fashion Event Stock

Inside back cover - no text as a seperate price list will sit here.

Outside back cover - I was thinking of having a collage of images worked into
the design but open to the designers input as well.
I also have another logo with phone number & web address
I would like on the back cover - Will be included in the files
provided.

I have a black background & white background version of my logo I will include both for the design work. I'm trying to get away from an all black design so if using the black logo I don't want a completely black page design, just becomes to heavy.

I'm redoing my website soon so please base the folder design around my logo text & colours not my current website as it's very outdated.

Logo brand guide is as follows

Main Font Font: Reislust
Main Font Color: #fff
Slogan Font Font: Ubuntu Bold
Monogram Font Font: Venti Medium
Container Color: #fff

Please respect the copyright on the images provided and delete all content once the design has been completed.
Thanks.

Need extra days to review

```html
<!DOCTYPE html>
<html lang="en">
<head>
<meta charset="utf-8">
<title>Northlight Studio – Presentation Folder</title>
<link href="https://fonts.googleapis.com/css2?family=Montserrat:wght@400;600&family=Lato:wght@400;700&display=swap" rel="stylesheet">
<style>
  :root{
    --stage:#5f5f5f;
    --black:#0b0b0b;
    --ink:#1c1c1c;
    --gold:#c4974f;
    --gold-panel:#b58a4c;
    --paper:#ffffff;
    --muted:#555555;
  }
  *{box-sizing:border-box;margin:0;padding:0}
  html,body{width:960px;height:1200px;overflow:hidden;background:var(--stage)}
  body{position:relative;font-family:'Lato',sans-serif}
  .spread{position:absolute;left:100px;width:760px;height:557px;display:flex;box-shadow:0 8px 24px rgba(0,0,0,.35)}
  .spread--inside{top:28px}
  .spread--outside{top:615px}
  .page{position:relative;width:380px;height:557px;overflow:hidden}

  /* brand lockup */
  .brand{display:flex;align-items:center;gap:10px}
  .brand__mark{width:22px;height:22px;border:2px solid var(--gold)}
  .brand__name{font-family:'Montserrat',sans-serif;font-weight:400;letter-spacing:.18em;text-transform:uppercase;color:var(--gold);font-size:15px}
  .brand__tag{font-family:'Montserrat',sans-serif;font-size:6.5px;letter-spacing:.3em;text-transform:uppercase;color:var(--gold);margin-top:3px}

  /* inside left */
  .page--about{background:var(--paper);padding:44px 40px 0 40px}
  .about__title,.service__title{font-family:'Montserrat',sans-serif;font-weight:600;color:var(--gold);text-transform:uppercase;letter-spacing:.06em}
  .about__title{font-size:13px;margin-bottom:12px}
  .about__text{font-size:9px;line-height:1.6;color:var(--muted);margin-bottom:8px}
  .services{margin-top:22px}
  .service{margin-bottom:14px}
  .service__title{font-size:10px;margin-bottom:4px}
  .service__list{font-size:8.5px;color:var(--ink)}
  .page--about .brand{position:absolute;left:40px;bottom:48px}
  .page--about .brand__name{font-size:12px}
  .page--about .web{position:absolute;right:26px;bottom:20px;font-size:7px;color:var(--gold);letter-spacing:.08em}

  /* inside right */
  .page--pricing{background:var(--gold-panel)}
  .page--pricing .lockup{position:absolute;left:0;right:0;top:200px;display:flex;flex-direction:column;align-items:center}
  .page--pricing .brand__mark{border-color:#e9cf97}
  .page--pricing .brand__name,.page--pricing .brand__tag{color:#e9cf97}
  .pocket{position:absolute;left:0;bottom:0;width:380px;height:170px}

  /* outside */
  .page--back,.page--front{background:var(--black)}
  .back__scene{position:absolute;left:0;top:0;width:380px;height:300px;background:linear-gradient(180deg,#2c2c2c 0%,#1e1e1e 55%,var(--black) 100%)}
  .collage{position:absolute;border-radius:50%;border:2px solid #d9d9d9}
  .collage--back{left:-150px;top:110px;width:300px;height:300px;background:linear-gradient(160deg,#8a1f18 0%,#6b5a66 35%,#9a9aa6 55%,#b8322c 70%,#1d5fb0 100%)}
  .collage--back-inner{left:-60px;top:190px;width:150px;height:150px;background:linear-gradient(150deg,#7a6a80,#c9b9b5);border-color:#111}
  .page--back .lockup{position:absolute;left:55px;top:408px}
  .page--back .brand__name{font-size:12px}
  .contacts{position:absolute;left:36px;right:20px;bottom:32px;display:grid;grid-template-columns:1fr 1fr;gap:10px 14px}
  .contact{display:flex;align-items:center;gap:7px;color:#d8c7a3;font-size:9px}
  .contact svg{width:12px;height:12px;flex:none}

  .page--front .lockup{position:absolute;left:30px;top:30px}
  .collage--front{left:150px;top:130px;width:330px;height:330px;background:linear-gradient(150deg,#3d5aa8 0%,#c7ab75 30%,#8d6a44 55%,#d1c4b0 70%,#6a4a30 100%)}
  .collage--front-inner{left:252px;top:212px;width:175px;height:175px;background:radial-gradient(circle,#5a5a5a 0%,#d4d4d4 45%,#1a1a1a 80%);border-color:var(--black);border-width:5px}
  .page--front .web{position:absolute;left:60px;bottom:34px;font-family:'Montserrat',sans-serif;font-size:11px;letter-spacing:.22em;color:var(--gold)}
</style>
</head>
<body>

<section class="spread spread--inside">
  <div class="page page--about">
    <h2 class="about__title">About</h2>
    <p class="about__text">Northlight Studio is owned and operated by a professionally trained photographer with a lifelong love of images, light and the spaces people create.</p>
    <p class="about__text">Every brief is handled with care, from planning and lighting to final retouching, so each client receives images ready for print and web.</p>
    <p class="about__text">Experienced across many genres, the studio works with agents, hosts, architects and brands throughout the region and beyond.</p>
    <div class="services">
      <div class="service"><h3 class="service__title">Architecture</h3><p class="service__list">Commercial Residential Real Estate Drone Floorplans Accommodation</p></div>
      <div class="service"><h3 class="service__title">Corporate</h3><p class="service__list">Studio Headshots Environmental Portraits Staff Photography</p></div>
      <div class="service"><h3 class="service__title">Commercial</h3><p class="service__list">Product Advertising Fashion Event Stock</p></div>
    </div>
    <div class="brand"><span class="brand__mark"></span><span class="brand__name">Northlight Studio</span></div>
    <span class="web">www.northlightstudio.com.au</span>
  </div>
  <div class="page page--pricing">
    <div class="lockup">
      <div class="brand"><span class="brand__mark"></span><span class="brand__name">Northlight Studio</span></div>
      <div class="brand__tag">Architecture Corporate Commercial</div>
    </div>
    <svg class="pocket" viewBox="0 0 380 170" aria-hidden="true"><path d="M0 170 V70 Q0 0 80 0 Q140 0 160 50 L200 50 H380 V170 Z" fill="var(--black)"/></svg>
  </div>
</section>

<section class="spread spread--outside">
  <div class="page page--back">
    <div class="back__scene" role="img" aria-label="Faded dark photograph of a heritage building"></div>
    <div class="collage collage--back" role="img" aria-label="Circular collage: stage performer, man beside red sports car, blue classic car"></div>
    <div class="collage collage--back-inner" role="img" aria-label="Fashion portrait photograph"></div>
    <div class="lockup">
      <div class="brand"><span class="brand__mark"></span><span class="brand__name">Northlight Studio</span></div>
      <div class="brand__tag">Architecture Corporate Commercial</div>
    </div>
    <div class="contacts">
      <div class="contact"><svg viewBox="0 0 12 12"><circle cx="6" cy="6" r="6" fill="#3a3a3a"/><path d="M4 3.5l1 .2.4 1.3-.6.5a4 4 0 0 0 1.7 1.7l.5-.6 1.3.4.2 1-.8.6A5 5 0 0 1 3.4 4.3z" fill="#ddd"/></svg>0400 123 456</div>
      <div class="contact"><svg viewBox="0 0 12 12"><circle cx="6" cy="6" r="6" fill="#3a3a3a"/><rect x="3" y="4" width="6" height="4.2" fill="none" stroke="#ddd" stroke-width=".8"/><path d="M3 4l3 2.3L9 4" fill="none" stroke="#ddd" stroke-width=".8"/></svg>info@northlightstudio.com.au</div>
      <div class="contact"><svg viewBox="0 0 12 12"><circle cx="6" cy="6" r="6" fill="#3a3a3a"/><path d="M6 9.5S3.8 7 3.8 5.2a2.2 2.2 0 0 1 4.4 0C8.2 7 6 9.5 6 9.5z" fill="#ddd"/><circle cx="6" cy="5.2" r=".8" fill="#3a3a3a"/></svg>12 Elm Rd Westbury, VIC, 3000</div>
      <div class="contact"><svg viewBox="0 0 12 12"><circle cx="6" cy="6" r="6" fill="#3a3a3a"/><circle cx="6" cy="6" r="3" fill="none" stroke="#ddd" stroke-width=".8"/><path d="M3 6h6M6 3v6" stroke="#ddd" stroke-width=".6"/></svg>www.northlightstudio.com.au</div>
    </div>
  </div>
  <div class="page page--front">
    <div class="lockup">
      <div class="brand"><span class="brand__mark"></span><span class="brand__name">Northlight Studio</span></div>
      <div class="brand__tag">Architecture Corporate Commercial</div>
    </div>
    <div class="collage collage--front" role="img" aria-label="Circular collage: heritage homestead at dusk, hotel bedroom, custom hot rod"></div>
    <div class="collage collage--front-inner" role="img" aria-label="Product photograph of a luxury wristwatch"></div>
    <span class="web">www.northlightstudio.com.au</span>
  </div>
</section>

</body>
</html>
```